Business Card for Quillmark Ledger - A cannabis publication for executives.

I'd like some business cards for Quillmark Ledger. The logo is done (great job!) and I need a card design I will use with PRINTLY. I made it a short project to allow time for printing before an event. These will be standard sized cards (final artwork size 3.66" x 2.16" at 300dpi) with a final card size of 3.5" x 2.0". (See PRINTLY.com if you need more info.) I might try rounded corners but am not sure yet. I think the design will work okay with rounded.

Quillmark Ledger will be a bi-weekly publication for the cannabis industry. It is targeted to investors and industry executives, not consumers or pot smokers. So our market is more B2B. However I am open to creativity and making the card something people remark on.

My contact for card:

Dana Merrow
Founder/CEO
dana@quillmarkledger.example

2740 Harlow Avenue
Boston MA 02135
(617)555-0194

Target Market(s)

Executives, Industry people and investors in the Cannabis sector.

Contact Information for Business Card

PRINTLY does do double sided and the second side can be the same or different images. Only one side is required but use of the second side would be a bonus.

Font styles to use
Serif
Sans Serif
Decorative

Colors

Designer to choose colors to be used in the design.

Requirements
Must have
• Logo, contact info
Nice to have
• Style and design to make the card stand out in a crowd.

```html
<!DOCTYPE html>
<html lang="en">
<head>
<meta charset="utf-8">
<title>Quillmark Ledger — Business Card</title>
<link rel="stylesheet" href="https://fonts.googleapis.com/css2?family=Lato:wght@400;700&display=swap">
<style>
  :root {
    --bg: #3b3b3b;
    --brand-blue: #1c75bc;
    --brand-green: #7cb036;
    --white: #ffffff;
    --bubble: rgba(255, 255, 255, 0.12);
  }
  * { margin: 0; padding: 0; box-sizing: border-box; }
  html, body {
    width: 1138px;
    height: 1200px;
    overflow: hidden;
    background: var(--bg);
    font-family: "Lato", sans-serif;
  }
  .card {
    position: absolute;
    left: 234px;
    width: 670px;
    height: 382px;
    border-radius: 16px;
    overflow: hidden;
    background: var(--brand-blue);
    color: var(--white);
    box-shadow: 0 4px 12px rgba(0, 0, 0, 0.35);
  }
  .card--front { top: 198px; }
  .card--back { top: 617px; }
  .card__art { position: absolute; inset: 0; }

  .brand-name {
    position: absolute;
    font-weight: 700;
    white-space: nowrap;
    letter-spacing: -0.5px;
  }
  .card--front .brand-name {
    left: 30px;
    top: 38px;
    font-size: 46px;
    color: var(--brand-blue);
  }

  .person {
    position: absolute;
    left: 33px;
    top: 216px;
  }
  .person__name { font-size: 26px; font-weight: 700; line-height: 32px; }
  .person__role { font-size: 18px; font-weight: 400; line-height: 22px; }

  .contact {
    position: absolute;
    left: 35px;
    top: 292px;
    list-style: none;
    font-size: 18px;
    line-height: 23px;
  }
  .contact li { display: flex; align-items: center; gap: 8px; }
  .contact svg { width: 15px; height: 15px; flex: none; }

  .address {
    position: absolute;
    right: 33px;
    top: 315px;
    font-style: normal;
    text-align: right;
    font-size: 18px;
    line-height: 23px;
  }

  .back-brand {
    position: absolute;
    left: 0;
    right: 0;
    top: 160px;
    display: flex;
    justify-content: center;
    align-items: center;
    gap: 18px;
  }
  .back-brand__dot {
    width: 56px;
    height: 56px;
    border-radius: 50%;
    background: var(--brand-green);
  }
  .card--back .brand-name {
    position: static;
    font-size: 52px;
    color: var(--white);
  }
  .back-url {
    position: absolute;
    left: 0;
    right: 0;
    top: 341px;
    text-align: center;
    font-size: 18px;
  }
  .back-url .accent { color: var(--brand-green); }
</style>
</head>
<body>

<section class="card card--front" aria-label="Card front">
  <svg class="card__art" viewBox="0 0 670 382" width="670" height="382" aria-hidden="true">
    <path d="M0,0 H380 C520,8 660,40 654,150 C648,240 580,272 510,266 C430,260 380,230 300,190 C230,155 170,140 120,152 C70,164 30,190 0,218 Z" fill="#ffffff"/>
    <path class="wave-gap" d="M380,0 C520,8 660,40 654,150 C648,240 580,272 510,266 C430,260 380,230 300,190 C230,155 170,140 120,152 C70,164 30,190 0,218" fill="none" stroke="#ffffff" stroke-width="22"/>
    <path class="wave-band" d="M380,0 C520,8 660,40 654,150 C648,240 580,272 510,266 C430,260 380,230 300,190 C230,155 170,140 120,152 C70,164 30,190 0,218" fill="none" stroke="#7cb036" stroke-width="12"/>
  </svg>
  <svg style="position:absolute;left:302px;top:150px" width="68" height="60" viewBox="0 0 68 60" role="img" aria-label="Green leaf illustration">
    <ellipse cx="34" cy="32" rx="30" ry="24" fill="#7cb036"/>
  </svg>

  <div class="brand-name">Quillmark Ledger</div>

  <div class="person">
    <div class="person__name">Dana Merrow</div>
    <div class="person__role">Founder/CEO</div>
  </div>

  <ul class="contact">
    <li>
      <svg viewBox="0 0 16 16" aria-hidden="true"><path d="M4 1 L6.5 4.5 L5 6.5 C6 8.8 7.4 10.2 9.5 11 L11.5 9.5 L15 12 L13 15 C7 15 1 9 1 3 Z" fill="#fff"/></svg>
      (617)555-0194
    </li>
    <li>
      <svg viewBox="0 0 16 16" aria-hidden="true"><rect x="1" y="3" width="14" height="10" fill="#fff"/><path d="M1 3 L8 9 L15 3" fill="none" stroke="#1c75bc" stroke-width="1.3"/></svg>
      dana@quillmarkledger.example
    </li>
    <li>
      <svg viewBox="0 0 16 16" aria-hidden="true"><g fill="none" stroke="#fff" stroke-width="1.2"><circle cx="8" cy="8" r="7"/><ellipse cx="8" cy="8" rx="3" ry="7"/><path d="M1 8 H15 M2 4.5 H14 M2 11.5 H14"/></g></svg>
      www.quillmarkledger.example
    </li>
  </ul>

  <address class="address">
    2740 Harlow Avenue<br>
    Boston MA 02135
  </address>
</section>

<section class="card card--back" aria-label="Card back">
  <svg class="card__art" viewBox="0 0 670 382" width="670" height="382" aria-hidden="true">
    <g fill="rgba(255,255,255,0.12)">
      <circle cx="664" cy="199" r="18"/>
      <circle cx="608" cy="259" r="18"/>
      <circle cx="641" cy="316" r="18"/>
      <circle cx="586" cy="367" r="18"/>
    </g>
  </svg>
  <div class="back-brand">
    <span class="back-brand__dot" aria-hidden="true"></span>
    <span class="brand-name">Quillmark Ledger</span>
  </div>
  <div class="back-url">www.quillmark<span class="accent">ledger</span>.example</div>
</section>

</body>
</html>
```